CRPG is needing business cards, and stationary created.

Pixel Forge created a logo for our business, and now we are wanting business cards, and stationary. I have included two designs of the same logo. Please feel free to use them as you want. The name of the company is Cedar Ridge Property Group LLC, the address is 812 NE Willow Ln., Suite 9, the city & state is Bend, Oregon, zip code is 97815, Telephone number is 541-327-4489, Fax number is 541-327-6051, the name on the business card is Carl Whitby CMCA

Industry/Entity Type

Property Management

Contact Information for Business Card

The card needs to look professional. Upscale.

Requirements
Must have
• The colors we are using are on the logo that has been uploaded.

```html
<!DOCTYPE html>
<html lang="en">
<head>
<meta charset="utf-8">
<title>Cedar Ridge Property Group — Business Cards</title>
<link rel="stylesheet" href="https://fonts.googleapis.com/css2?family=Source+Sans+3:wght@400;600;700&display=swap">
<style>
  :root {
    --teal: #1a8f7a;
    --slate: #3c4858;
    --ink: #4a4f55;
    --paper: #ffffff;
    --backdrop: #2b2b2d;
  }
  * { box-sizing: border-box; margin: 0; padding: 0; }
  html, body {
    width: 1200px; height: 892px; overflow: hidden;
    background: var(--backdrop);
    font-family: "Source Sans 3", sans-serif;
  }
  .canvas { position: relative; width: 1200px; height: 892px; }
  .card {
    position: absolute; width: 520px; height: 297px;
    background: var(--paper); overflow: hidden;
    box-shadow: 0 10px 28px rgba(0,0,0,.45);
  }
  .card--back { left: 70px; top: 130px; }
  .card--front { left: 610px; top: 460px; }

  .brand { display: flex; align-items: center; gap: 12px; }
  .brand__mark { width: 34px; height: 34px; background: var(--slate); }
  .brand__name {
    font-weight: 700; color: var(--teal);
    font-size: 38px; letter-spacing: 1px; line-height: 1;
    text-transform: uppercase;
  }
  .card--back .brand { position: absolute; left: 0; right: 0; top: 100px; justify-content: center; }
  .website {
    position: absolute; left: 0; right: 0; bottom: 40px; text-align: center;
    color: var(--ink); font-size: 15px; letter-spacing: 2.5px;
  }

  .corner { position: absolute; right: 0; top: 0; }
  .card--front .brand { position: absolute; left: 30px; top: 60px; }
  .card--front .brand__name { font-size: 30px; }
  .card--front .brand__mark { width: 26px; height: 26px; }
  .contact { position: absolute; left: 30px; top: 150px; color: var(--ink); font-size: 17px; line-height: 1.25; }
  .contact__name { color: var(--teal); font-weight: 700; font-size: 22px; margin-bottom: 4px; }
  .contact__lines { margin-bottom: 6px; }
  .contact__label { color: var(--teal); font-weight: 700; }
</style>
</head>
<body>
<main class="canvas">
  <section class="card card--back" aria-label="Card back">
    <div class="brand">
      <span class="brand__mark"></span>
      <span class="brand__name">Cedar Ridge</span>
    </div>
    <p class="website">www.cedarridgepropertygroup.com</p>
  </section>

  <section class="card card--front" aria-label="Card front">
    <svg class="corner" width="240" height="297" viewBox="0 0 240 297" aria-hidden="true">
      <polygon points="0,0 240,0 240,190" fill="var(--teal)"/>
    </svg>
    <div class="brand">
      <span class="brand__mark"></span>
      <span class="brand__name">Cedar Ridge</span>
    </div>
    <div class="contact">
      <p class="contact__name">Carl Whitby CMCA</p>
      <p class="contact__lines">812 NE Willow Ln., Suite 9<br>Bend, Oregon 97815</p>
      <p><span class="contact__label">Phone:</span> 541-327-4489</p>
      <p><span class="contact__label">Fax:</span> 541-327-6051</p>
    </div>
  </section>
</main>
</body>
</html>
```